flyer for a contemporary music concert: GILDED TALL HORN HAZE

We are an ensemble of contemporary music turning 10 years in 2019. Our next concert is a cooperation with the northernmost chamber orchestra, the fjordvik consortia. Our program is with live electronic, video and a big setup (like bigband). We would like to have a flyer promoting this event.- The speciality is contemporary on the on the one hand but this particulary program is quite popular with the big setup, the brass, the electronics and video - it aims for a club-audience more than the "normal" classical music audience.

Target Market(s)

young audience interested in going to concerts, club generation 20-30 years

Font styles to use
Serif
Sans Serif

Colors

Designer to choose colors to be used in the design.

Requirements
Must have
• feeling of contemporary art, we are playing classical music but pieces of composers that are still alive - design should transport this.
• here is the link to the concertplace:
• https://www.kornwiese.org/de/event/gilded-tall-horn-haze/
• here is the link to the ensemble:
• www.lagatosombria.de
• format: "DIN lang" (105mm x 210mm)
• two pages: front and backsinde.
Nice to have
• could be crazy, not too classical
• you could use the attached images, but no need at all! Important are just the two logos of the ensembles (logo1, logo2) and the logos of the funding partners (logo3, logo4)
Should not have
• - no clipart, musical symbols like notes, key symbols or something like this you would expect in a poster for a music school advertising
• - no hand writing font

```html
<!DOCTYPE html>
<html lang="de">
<head>
<meta charset="utf-8">
<title>Gilded Tall Horn Haze – Flyer</title>
<link href="https://fonts.googleapis.com/css2?family=Oswald:wght@400;500&family=Open+Sans:wght@400;600&family=PT+Serif&display=swap" rel="stylesheet">
<style>
:root{
  --page:#e4e4e2;
  --paper:#ffffff;
  --dark-top:#3d4046;
  --dark-bottom:#1f2125;
  --ice:#7cc6ea;
  --ice-soft:#a9daf2;
  --ink:#2b2f36;
  --muted:#9aa0a8;
  --rule:#6d737b;
}
*{box-sizing:border-box;margin:0;padding:0}
html,body{width:1200px;height:1147px;overflow:hidden}
body{background:var(--page);font-family:"Open Sans",Arial,sans-serif;position:relative}
.flyer{position:absolute;top:77px;width:480px;height:955px;background:var(--paper);overflow:hidden;box-shadow:0 4px 14px rgba(0,0,0,.18)}
.flyer--front{left:83px}
.flyer--back{left:621px}
.abs{position:absolute}
.dark-panel{position:absolute;left:0;right:0;background:linear-gradient(180deg,var(--dark-top),var(--dark-bottom))}
.wave{position:absolute;left:0;width:480px}

/* front */
.brand-name{top:108px;left:0;width:480px;text-align:center;font-family:"PT Serif",Georgia,serif;font-size:30px;letter-spacing:1px;color:#34465a}
.ensemble-photo{top:150px;left:0;width:480px;height:280px;background:linear-gradient(180deg,#9fb4c9 0%,#c8d5e1 45%,#3a3e45 62%,#dfe7ee 74%,#f4f7f9 100%)}
.front-panel{top:420px;height:470px}
.stage-photo{top:398px;left:328px;width:144px;height:144px;border-radius:50%;border:6px solid var(--paper);background:radial-gradient(circle at 50% 45%,#b5704a,#5a2a1c 55%,#1b0f0c)}
.event-title{left:0;width:480px;text-align:center;font-family:"Oswald",Arial,sans-serif;font-weight:500;color:#fff;letter-spacing:.5px}
.front-title{top:555px;font-size:40px;line-height:1}
.lineup{top:608px;left:0;width:480px;text-align:center;color:#fff;font-size:16px}
.featuring{top:632px;left:0;width:480px;text-align:center;color:var(--ice);font-size:13px}
.rule{position:absolute;height:1px;background:var(--rule)}
.date-line{top:675px;left:0;width:480px;text-align:center;font-family:"Oswald",Arial,sans-serif;font-size:16px;color:#fff}
.programme{top:728px;left:40px;width:400px;border-collapse:collapse;font-size:11px;line-height:1.25}
.programme td{padding:2px 0;vertical-align:top}
.programme .composer{color:var(--ice);text-align:right;width:130px;padding-right:12px}
.programme .work{color:#fff}

/* shared footer */
.phone-pill{top:860px;left:30px;width:420px;height:40px;border-radius:20px;background:var(--ice-soft);display:flex;align-items:center;justify-content:center;gap:10px;color:#fff;font-size:18px}
.phone-pill svg{width:20px;height:20px}
.event-url{top:918px;left:0;width:480px;text-align:center;color:var(--ink);font-size:14px;font-weight:600}

/* back */
.musicians-photo{top:0;left:0;width:480px;height:360px;background:linear-gradient(180deg,#d9d9d9 0%,#bdbdbd 25%,#8e8f92 45%,#4d4f54 62%,#2c2d31 80%,#5e6166 100%)}
.back-panel{top:345px;height:545px}
.back-title{top:390px;font-size:44px;line-height:1}
.description{top:460px;left:30px;width:420px;color:#e9ebee;font-size:12.6px;line-height:1.38;text-align:justify;hyphens:auto}
.description p+p{margin-top:14px}
.partners{top:755px;left:30px;width:420px;display:flex;align-items:center;justify-content:center;gap:16px}
.partner-badge{background:#8d939b;opacity:.75}
.partner-badge--text{width:70px;height:26px}
.partner-badge--city{width:70px;height:34px}
.partner-name{display:flex;align-items:center;gap:8px;color:#cfd3d8;font-size:15px;font-weight:600;letter-spacing:.5px}
.partner-name span.mark{width:24px;height:24px;background:#cfd3d8}
.social{top:815px;left:0;width:480px;display:flex;justify-content:center;gap:6px}
.social span{width:18px;height:18px;background:var(--ice)}
</style>
</head>
<body>

<section class="flyer flyer--front">
  <div class="abs ensemble-photo" role="img" aria-label="Ensemble members standing in a row on a frozen lake under a pale winter sky"></div>
  <svg class="wave" style="top:0;height:240px" viewBox="0 0 480 240" preserveAspectRatio="none">
    <path d="M0 0H480V200C380 160 320 150 240 185C160 220 80 215 0 190Z" fill="#fff"/>
    <path d="M0 196C80 222 160 226 240 192C320 158 380 168 480 206" fill="none" stroke="#7cc6ea" stroke-width="4"/>
  </svg>
  <div class="abs brand-name">FJORDVIK CONSORTIA</div>

  <div class="dark-panel front-panel"></div>
  <svg class="wave" style="top:395px;height:70px" viewBox="0 0 480 70" preserveAspectRatio="none">
    <path d="M0 20C120 0 200 45 300 40C380 36 430 10 480 25V70H0Z" fill="#3d4046"/>
    <path d="M0 18C120 -2 200 43 300 38C380 34 430 8 480 23" fill="none" stroke="#a9daf2" stroke-width="3"/>
  </svg>
  <div class="abs stage-photo" role="img" aria-label="Concert stage in warm red light with a screen projection"></div>

  <h1 class="abs event-title front-title">GILDED TALL HORN HAZE</h1>
  <p class="abs lineup">La Gato Sombría und Fjordvik Consortia</p>
  <p class="abs featuring">Featuring Ola Brekke Lundan</p>
  <div class="rule" style="top:660px;left:40px;width:400px"></div>
  <p class="abs date-line">08. NOVEMBER 2019, FESTSPIELHAUS KORNWIESE</p>
  <div class="rule" style="top:708px;left:40px;width:400px"></div>
  <table class="abs programme">
    <tr><td class="composer">Ivar Solheim:</td><td class="work">Saxophonkonzert (2018 UA) 15'<br>Der Komponist ist anwesend.</td></tr>
    <tr><td class="composer">Konrad Weil:</td><td class="work">... loops for Al Mortensen (2014) 17'</td></tr>
    <tr><td class="composer">Matthias Gruber:</td><td class="work">take nine for twelve (2012) 12'</td></tr>
    <tr><td class="composer">Daniel Kerr:</td><td class="work">I fought the law (1998) 6'</td></tr>
    <tr><td class="composer">Steinar Rohde:</td><td class="work">Antarctica (2016) 13'</td></tr>
  </table>

  <div class="abs phone-pill">
    <svg viewBox="0 0 24 24"><circle cx="12" cy="12" r="10.5" fill="none" stroke="#fff" stroke-width="1.6"/><path d="M8.6 7.2l1.6-.4 1 2.4-1.1.9c.6 1.3 1.5 2.2 2.8 2.8l.9-1.1 2.4 1-.4 1.6c-.2.6-.8.9-1.4.8-3.1-.6-5.4-2.9-6-6-.1-.6.2-1.2.8-1.4z" fill="#fff"/></svg>
    <span>+30 210 5571904</span>
  </div>
  <p class="abs event-url">https://www.kornwiese.org/de/event/gilded-tall-horn-haze/</p>
</section>

<section class="flyer flyer--back">
  <div class="abs musicians-photo" role="img" aria-label="Musicians with their instruments above a misty mountain landscape, ensemble group below"></div>

  <div class="dark-panel back-panel"></div>
  <svg class="wave" style="top:300px;height:70px" viewBox="0 0 480 70" preserveAspectRatio="none">
    <path d="M0 40C60 55 120 30 200 35C300 42 400 15 480 20V70H0Z" fill="#3d4046"/>
    <path d="M0 38C60 53 120 28 200 33C300 40 400 13 480 18" fill="none" stroke="#a9daf2" stroke-width="4"/>
  </svg>

  <h2 class="abs event-title back-title">GILDED TALL HORN HAZE</h2>
  <div class="rule" style="top:440px;left:80px;width:320px"></div>
  <div class="abs description">
    <p>In dem gemeinsamen Konzertprojekt Gilded Tall Horn Haze präsentiert das Ensemble für aktuelle Musik La Gato Sombría aus Dresden gemeinsam mit dem nördlichsten Kammerorchester der Welt, der Fjordvik Consortia aus Tromsø, Musik, die sich am wohlsten zwischen allen Stühlen fühlt. Nicht nur geographisch, sondern auch stilistisch werden Grenzen überschritten: Klassische Musik, knarzige Avantgarde, furiose Jazz- und groovige Rocksounds, geballte rhythmische Prägnanz und strukturelle Komplexität, dazu Live-Elektronik und Filminstallationen.</p>
    <p>Zum 10-jährigen Jubiläum des Dresdner Ensembles beschenkt es damit die Hörer*innen und sich selbst gleichermaßen. Zudem wird eine Kooperation fortgesetzt, die im letzten Jahr mit dem Programm Nordklang Arktis erfolgreich begann.</p>
  </div>

  <div class="abs partners">
    <span class="partner-badge partner-badge--text"></span>
    <span class="partner-badge partner-badge--city"></span>
    <span class="partner-name"><span class="mark"></span>LA GATO SOMBRÍA</span>
  </div>
  <div class="abs social"><span></span><span></span><span></span><span></span></div>

  <div class="abs phone-pill">
    <svg viewBox="0 0 24 24"><circle cx="12" cy="12" r="10.5" fill="none" stroke="#fff" stroke-width="1.6"/><path d="M8.6 7.2l1.6-.4 1 2.4-1.1.9c.6 1.3 1.5 2.2 2.8 2.8l.9-1.1 2.4 1-.4 1.6c-.2.6-.8.9-1.4.8-3.1-.6-5.4-2.9-6-6-.1-.6.2-1.2.8-1.4z" fill="#fff"/></svg>
    <span>+30 210 5571904</span>
  </div>
  <p class="abs event-url">https://www.kornwiese.org/de/event/gilded-tall-horn-haze/</p>
</section>

</body>
</html>
```